VistaWave webpage - Design only no coding required

Please refer to "web content" uploaded 23rd Sep for content

We are a digital signage company based in Jakarta, Indonesia.

Our core business is placement of LCD Tv's in waiting rooms of various hospitals in Indonesia which plays educational videos regarding various health topics (prescription/ethical medicines), OTC drugs TVC and other FMCG and ads.

Our client portfolio consists of the worlds biggest and well known Pharmaceutical companies and also local pharmaceutical companies.

Other parts of our business are as follows:
- Patient symposiums
- Booths for product activation
- Queuing systems that we have developed in house that use an android tablet and connect to our TV's
- Branding. eg. Lift doors, banners (static signage)
- Hospital management software. Specially developed software that comes in a generic format and needs to be customized to suit each hospital. It manages everything for phone/web booking, queues, registration, patient records, doctors schedules, referrals, pharmacy and inventory and checkout/payments.

We are after a website redesign that is visually attractive and modern as we also deal with many advertising agencies.

Our logo is orange and black, however the black & white can be reversed if necessary.

Pages will need to be available in English & Bahasa Indonesia language formats.

I am happy to answer any questions asap, i can be contacted at info@vistawave.example.co.id

current site (www.vistawave.example.co.id)

Target Market(s)

Mainly our business is B2B dealing with advertising clients either directly or through ad agencies.

The other aspect of our target market is hospitals where we place our screens.

There is (but not largely) and consumer audience.

In summary:
We have the following target markets:
1. Advertisers/ad agencies
2. Hospitals that wish to use our business model to display content to their patients 3. We are in a developing country however most of our viewers and clients are from a high demographic profile

Industry/Entity Type

Pharmaceutical

Requirements
Must have
• We will require duplicates of the pages in English & Bahasa Indonesia

I would like the initial designs with a focus on being clean yet bold and emphasis on typography.

The following pages will be required (but not limited to) to qualify for the prize:

-Home

- About Us

- Services
(sub pages)
=Digital Signage
=Video Content Production
=Hospital Branding
=Event Management
=Seminar
=Queue System
=Hospital Management Software

-Why Choose Us?

- Contact Us

- Clients & Partners

- Gallery

Based on the "Nice to haves" site examples we do not necessarily require pictures of our LCD's/content on the main page(s) and would be happy to purchase required stock photos if needed/agreed.

We definitely want a modern feel and do not wish to overload with too much info on the main page.

(Please note the text in the attached file will most likely be changed once we have a design concept, probably less text)

Webpages we like:
http://www.plumbrookstudio.example.com/
http://kettlefinch.example.com

Nice to have
• This is some of the international players which we want our site to look like:
www.skylarkdisplays.example.com.au
http://www.marvellepanels.example.co.uk/
www.tundralens.example.com/

Should not have
• We prefer not to have old outdated fonts and a website that resembles anything like the current one, we are after a modern and professional feel.
These are some of our relative competitors of which we DO NOT want our website looking like but as a reference:
http://quillcare-global.example.com/index.html
http://rtb.example.co.id/

```html
<!DOCTYPE html>
<html lang="en">
<head>
<meta charset="utf-8">
<title>VistaWave Digital Signage</title>
<link rel="stylesheet" href="https://fonts.googleapis.com/css2?family=Crimson+Text:wght@400;600&family=Questrial&family=Arimo:wght@400;700&display=swap">
<style>
:root{
  --orange:#f2a516;
  --orange-deep:#d98b0a;
  --button:#f0a420;
  --button-dark:#d38a0b;
  --dark:#1c1c1c;
  --darker:#121212;
  --grey-band:#e6e5e3;
  --text-grey:#5a5a5a;
  --white:#ffffff;
}
*{margin:0;padding:0;box-sizing:border-box}
html,body{width:816px;height:1200px;overflow:hidden;background:var(--white)}
body{position:relative;font-family:'Arimo',Arial,sans-serif;color:var(--text-grey)}
.abs{position:absolute}

/* navigation */
.topbar{left:0;top:0;width:816px;height:51px;background:linear-gradient(#222,#151515)}
.brand{left:46px;top:15px;display:flex;align-items:center;gap:7px;color:var(--white);font-family:'Arimo',sans-serif;font-weight:700;font-size:15px}
.brand-mark{width:14px;height:14px;background:var(--orange)}
.nav{right:33px;top:19px;display:flex;font-family:'Crimson Text',serif;font-size:13px;color:#e9e9e9}
.nav span{padding:1px 6px;margin-left:12px}
.nav .current{background:var(--orange);color:var(--white);border-radius:1px}

/* hero */
.hero{left:0;top:51px;width:816px;height:271px;background:
  radial-gradient(ellipse at 75% 40%,#f0c870 0%,rgba(220,170,80,.6) 30%,transparent 60%),
  linear-gradient(90deg,#6d5434 0%,#a9895c 18%,#c8a66a 45%,#dcb56c 70%,#b88a45 100%)}
.hero-title{left:0;top:83px;width:816px;text-align:center;color:var(--white);font-family:'Questrial',sans-serif}
.hero-title .welcome{font-size:12px;display:flex;justify-content:center;align-items:center;gap:6px}
.hero-title .welcome i{display:block;width:88px;border-top:1px solid rgba(255,255,255,.8);border-bottom:1px solid rgba(255,255,255,.5);height:3px}
.hero-title h1{font-weight:400;font-size:29px;line-height:33px;margin-top:2px;text-shadow:0 1px 3px rgba(0,0,0,.3)}
.hero-rule{left:289px;top:171px;width:238px;height:3px;border-top:1px solid rgba(255,255,255,.8);border-bottom:1px solid rgba(255,255,255,.5)}

.service-band{left:0;top:322px;width:816px;height:121px;background:var(--dark)}
.service-photo{width:138px;height:138px;border-radius:50%;overflow:hidden}
.service-photo .fill{width:100%;height:100%}
.service-ring{width:138px;height:138px;border-radius:50%;border:3px solid transparent}
.ring-orange{border-bottom-color:var(--orange);border-left-color:var(--orange)}
.ring-white{border-bottom-color:#eee;border-right-color:#eee}
.service-label{width:180px;text-align:center;font-family:'Crimson Text',serif;font-size:14.5px;line-height:18px;color:var(--white)}
.service-label em{font-style:normal;color:var(--orange)}

.blur-strip{left:0;top:443px;width:816px;height:42px;background:linear-gradient(90deg,#8a6a44,#d9c4a0 20%,#9b7a55 40%,#e6d2b0 60%,#7d5c38 80%,#c79c5c)}
.strip-edge{left:0;top:485px;width:816px;height:4px;background:#2a2420}

/* about */
.about{left:0;top:489px;width:816px;height:287px;background:var(--orange)}
.about-edge{left:0;top:776px;width:816px;height:7px;background:#c99434}
.section-title{font-family:'Crimson Text',serif;font-weight:400;font-size:19px;color:#222}
.rule{height:1px;background:rgba(0,0,0,.12)}
.about .rule{background:rgba(255,255,255,.45)}
.about-frame{left:99px;top:79px;width:154px;height:153px;background:#f8c55a;padding:7px}
.about-frame .fill{width:100%;height:100%;background:linear-gradient(160deg,#5a4636,#b7977a 45%,#6b4a33)}
.about-copy{left:269px;top:73px;width:473px;font-size:10.2px;line-height:17.6px;color:var(--white);text-align:justify}
.about-copy .lead{font-weight:700;margin-bottom:17.6px}

/* news */
.news-title{left:108px;top:804px}
.news-rule{left:99px;top:834px;width:650px}
.article{top:848px;width:248px}
.article-photo{left:0;top:0;width:95px;height:94px;background:linear-gradient(135deg,#c9c2b4,#e8d640 45%,#8a8f9c)}
.article h3{position:absolute;left:108px;top:0;font-weight:400;font-size:10.4px;color:var(--orange);white-space:nowrap}
.article .date{position:absolute;left:108px;top:14px;font-size:8.6px;color:#999}
.article .intro{position:absolute;left:108px;top:27px;width:140px;font-size:8.4px;line-height:14.4px;text-align:justify}
.article .more{position:absolute;left:1px;top:101px;width:247px;font-size:8.4px;line-height:14.4px}
.btn{position:absolute;top:153px;width:70px;height:23px;font-size:8.4px;color:var(--white);display:flex;align-items:center;justify-content:center}
.btn-read{left:95px;background:var(--button)}
.btn-share{left:172px;background:var(--button-dark)}
.view-all{left:621px;top:1047px;font-size:8.6px}
.bottom-rule{left:99px;top:1062px;width:650px}

/* partners */
.partners{left:0;top:1078px;width:816px;height:92px;background:var(--grey-band);display:flex;align-items:center;justify-content:space-around;padding:0 90px 0 100px}
.partner{font-family:'Arimo',sans-serif;font-weight:700;font-size:15px;color:#666;display:flex;align-items:center;gap:6px}
.partner .dot{width:12px;height:12px;border-radius:50%;background:#777}

/* footer */
.footer{left:0;top:1170px;width:816px;height:30px;background:var(--darker)}
.copyright{left:59px;top:9px;font-size:8.4px;color:#bbb}
.social{right:70px;top:5px;display:flex;gap:6px}
.social span{width:19px;height:19px;border-radius:50%}
</style>
</head>
<body>
<header class="abs topbar">
  <div class="abs brand"><span class="brand-mark"></span>VistaWave</div>
  <nav class="abs nav"><span class="current">Home</span><span>About us</span><span>Services</span><span>Why Choose us</span><span>Gallery</span><span>Contact us</span></nav>
</header>

<section class="abs hero" role="img" aria-label="Blurred photo of a hospital waiting room with a wall-mounted screen"></section>
<div class="abs hero-title">
  <div class="welcome"><i></i>Welcome to<i></i></div>
  <h1>VistaWave Digital<br>Signage</h1>
</div>
<div class="abs hero-rule"></div>

<div class="abs service-band"></div>

<div class="abs service-photo" style="left:94px;top:247px"><div class="fill" role="img" aria-label="Photo of a presentation team in a media studio" style="background:linear-gradient(160deg,#2f5db0,#c8d4e8 50%,#8a6f5c)"></div></div>
<div class="abs service-ring ring-orange" style="left:94px;top:247px"></div>
<div class="abs service-photo" style="left:259px;top:247px"><div class="fill" role="img" aria-label="Photo of a video camera crew on a set" style="background:linear-gradient(160deg,#1a1a1a,#6a6a6a 50%,#d8d8d8)"></div></div>
<div class="abs service-ring ring-white" style="left:259px;top:247px"></div>
<div class="abs service-photo" style="left:422px;top:247px"><div class="fill" role="img" aria-label="Photo for hospital branding" style="background:linear-gradient(160deg,#3a3a3a,#9a9a9a 50%,#ececec)"></div></div>
<div class="abs service-ring ring-orange" style="left:422px;top:247px"></div>
<div class="abs service-photo" style="left:584px;top:247px"><div class="fill" role="img" aria-label="Photo of a queue number display screen" style="background:linear-gradient(170deg,#b89a7a,#2a3fa8 45%,#e8e1d6 75%)"></div></div>
<div class="abs service-ring ring-white" style="left:584px;top:247px"></div>

<div class="abs service-label" style="left:71px;top:397px">Media <em>Promotion</em></div>
<div class="abs service-label" style="left:236px;top:397px">Content Video<br><em>Production</em></div>
<div class="abs service-label" style="left:401px;top:397px">Hospital <em>Branding</em></div>
<div class="abs service-label" style="left:563px;top:397px">Queuing <em>System</em></div>

<div class="abs blur-strip" role="img" aria-label="Blurred photo strip of a lobby interior"></div>
<div class="abs strip-edge"></div>

<section class="abs about">
  <h2 class="abs section-title" style="left:108px;top:30px">About us</h2>
  <div class="abs rule" style="left:99px;top:59px;width:650px"></div>
  <div class="abs about-frame"><div class="fill" role="img" aria-label="Photo of patients seated in a hospital waiting room with a TV screen"></div></div>
  <div class="abs about-copy">
    <p class="lead">VistaWave owns and maintains a state of the art Digital Signage network, which is controlled using a campaign management software locally, and utilising latest internet technology can control screens anywhere in the world.</p>
    <p>Entrusted with managing content for the country’s and worlds most respected brands, VistaWave is therefore focused on total client satisfaction in all stages of service, our philosophy is simple “always deliver as stated”.</p>
    <p>Similar systems implemented in developed markets together with research conducted locally ensure that our niche however robust business model is ultimately sustainable. With the support of our host and advertising partners VistaWave foresees rapid growth in Indonesia.</p>
  </div>
  <div class="abs rule" style="left:99px;top:259px;width:650px"></div>
</section>
<div class="abs about-edge"></div>

<h2 class="abs section-title news-title">Latest News</h2>
<div class="abs rule news-rule"></div>

<article class="abs article" style="left:145px">
  <div class="abs article-photo" role="img" aria-label="Photo of two men using a touchscreen kiosk"></div>
  <h3>ARTICLE TITLE GOES HERE</h3>
  <div class="date">Sep 22 2013</div>
  <p class="intro">Lorem ipsum dolor sit amet, consectetur adipiscing elit. Vivamus sit amet rutrum nunc. Praesent vitae dui ut quam venenatis semper. Maecenas eleifend lectus</p>
  <p class="more">Lorem ipsum dolor sit amet, consectetur adipiscing elit. Vivamus sit amet rutrum nunc. Praesent vitae dui ut quam venenatis semper. Maecenas eleifend lectus nisi, et consectetur ipsum imperdiet</p>
  <span class="btn btn-read">read more</span><span class="btn btn-share">Share</span>
</article>
<article class="abs article" style="left:442px">
  <div class="abs article-photo" role="img" aria-label="Photo of two men using a touchscreen kiosk"></div>
  <h3>ARTICLE TITLE GOES HERE</h3>
  <div class="date">Sep 22 2013</div>
  <p class="intro">Lorem ipsum dolor sit amet, consectetur adipiscing elit. Vivamus sit amet rutrum nunc. Praesent vitae dui ut quam venenatis semper. Maecenas eleifend lectus</p>
  <p class="more">Lorem ipsum dolor sit amet, consectetur adipiscing elit. Vivamus sit amet rutrum nunc. Praesent vitae dui ut quam venenatis semper. Maecenas eleifend lectus nisi, et consectetur ipsum imperdiet</p>
  <span class="btn btn-read">read more</span><span class="btn btn-share">Share</span>
</article>
<div class="abs view-all">View All Articles</div>
<div class="abs rule bottom-rule"></div>

<section class="abs partners">
  <div class="partner">Medora</div>
  <div class="partner">Kestrel Capital</div>
  <div class="partner"><span class="dot"></span>Lumen Outdoor</div>
  <div class="partner">Adnexa</div>
  <div class="partner">Brightpost</div>
</section>

<footer class="abs footer">
  <div class="abs copyright">© Copyright 2013 - VistaWave Digital Signage. All Rights Reserved.</div>
  <div class="abs social">
    <span style="background:#3fa9e0"></span>
    <span style="background:#3b5ea8"></span>
    <span style="background:#f0f0f0"></span>
    <span style="background:#2a6fc9"></span>
    <span style="background:#f29a1f"></span>
  </div>
</footer>
</body>
</html>
```